Business card por a urban DJ, up scale audience target

Need a sober design, modern, conservative colors but i can consider some options, y play rnb, hip hop, EDM and top40.

Business card for contact and personal info, double sided, use logo attrached please; im 42 so i need a card acording to my age an target audience.

Target Market(s)

Adult people, up scale audience

Industry/Entity Type

Music Download

Contact Information for Business Card

Cel (318) 5024471963 www.kelvarodun.com

Requirements
Must have
• open mind
Nice to have
• open mind
Should not have
• DJ

```html
<!DOCTYPE html>
<html lang="en">
<head>
<meta charset="UTF-8">
<title>Kelvaro – Business Card</title>
<link href="https://fonts.googleapis.com/css2?family=Open+Sans:wght@400;700;800&display=swap" rel="stylesheet">
<style>
  :root {
    --ink: #2b2b2b;
    --paper: #f4f4f4;
    --paper-shade: #dcdcdc;
    --white: #ffffff;
    --stage: #e6e3de;
    --rule: #3a3a3a;
  }
  * { margin: 0; padding: 0; box-sizing: border-box; }
  html, body {
    width: 1200px; height: 780px; overflow: hidden;
    background: var(--stage);
    font-family: "Open Sans", Verdana, sans-serif;
  }
  .stage {
    position: relative; width: 1200px; height: 780px;
    display: flex; justify-content: center; align-items: center; gap: 60px;
  }
  .card {
    position: relative; width: 360px; height: 620px;
    box-shadow: 0 10px 28px rgba(0,0,0,0.25);
    overflow: hidden;
  }
  .card-front {
    background: radial-gradient(circle at 70% 30%, var(--white), var(--paper) 55%, var(--paper-shade));
    color: var(--ink);
  }
  .card-back {
    background: radial-gradient(circle at 30% 25%, #3a3a3a, var(--ink) 60%, #222);
    display: flex; align-items: center; justify-content: center;
  }
  .brand {
    display: flex; align-items: center; gap: 12px;
    font-weight: 800; font-size: 44px; letter-spacing: 1px;
  }
  .brand-mark { width: 22px; height: 22px; background: currentColor; }
  .card-front .brand { position: absolute; top: 78px; left: 0; right: 0; justify-content: center; color: var(--ink); }
  .card-back .brand { color: var(--white); }
  .identity { position: absolute; top: 210px; left: 0; right: 0; text-align: center; }
  .identity-name { font-weight: 800; font-size: 28px; letter-spacing: 1px; }
  .identity-title { font-size: 19px; margin-top: 2px; }
  .contact { position: absolute; top: 310px; left: 30px; right: 30px; text-align: center; }
  .contact-icon { display: block; width: 26px; height: 22px; margin: 0 auto 6px; }
  .contact-text { font-size: 24px; letter-spacing: 1px; }
  .contact-rule { height: 2px; background: var(--rule); margin: 10px 0 14px; }
  .contact-email { font-size: 22px; }
  .band {
    position: absolute; left: 0; right: 0; bottom: 0; height: 140px;
    background: var(--ink); color: var(--white);
    display: flex; align-items: center; justify-content: center;
    font-size: 22px; letter-spacing: 0.5px;
  }
</style>
</head>
<body>
<main class="stage">
  <section class="card card-front">
    <div class="brand"><span class="brand-mark"></span>KELVARO</div>
    <div class="identity">
      <p class="identity-name">EMPLOYEE NAME</p>
      <p class="identity-title">Development Manager</p>
    </div>
    <div class="contact">
      <svg class="contact-icon" viewBox="0 0 26 22" aria-hidden="true">
        <rect width="26" height="22" fill="#2b2b2b"/>
        <rect x="9" y="3" width="8" height="16" rx="1" fill="none" stroke="#fff" stroke-width="1.5"/>
        <rect x="11" y="5" width="4" height="5" fill="#fff"/>
      </svg>
      <p class="contact-text">(318) 5024471963</p>
      <div class="contact-rule"></div>
      <svg class="contact-icon" viewBox="0 0 26 22" aria-hidden="true">
        <rect width="26" height="22" fill="#2b2b2b"/>
        <rect x="5" y="6" width="16" height="11" fill="none" stroke="#fff" stroke-width="1.5"/>
        <path d="M5 6 L13 13 L21 6" fill="none" stroke="#fff" stroke-width="1.5"/>
      </svg>
      <p class="contact-email">your@kelvamail.com</p>
    </div>
    <div class="band">www.kelvarodun.com</div>
  </section>
  <section class="card card-back">
    <div class="brand"><span class="brand-mark"></span>KELVARO</div>
  </section>
</main>
</body>
</html>
```